WordPress website in children books redesign

We are personalised children storybook creators with a range of personalized books, music CDs and DVDs that are created for each child. We sell our concept through a license via distributors / entrepreneurs mainly based in France and Europe. We want to focus on selling B2C to parents and grandparents, looking to buy presents to their children aged 0 to 10 years old. Those present are educative, unique for each child, and they will learn to have fun and learn to have fun. I would like to redesign our WordPress website https://pebblelanternkids.co.uk/index.php We are a children in the world of books and music books: books, music CDs and DVDs looking for something a little more along the lines of our competitors. See ike www.quillotop.com, www.tavirosa.com, www.lecheminduvelours.com, https://www.lespetitsbrume.com/, https://tinselpaths.com/ Our current website is a bit too old fashioned so I am looking at a much more modern design Here is a link for a few products that are not available here: https://www.filecrate.example/sh/kq417dzopfrnwtb/BXPL3rYmOk2u-sVH4dQkLN-zb?dl=0 We have 2 sides in our website: B2C on the left side and B2B on the right site; B2B is for distributors that are entrepreneurs buying our concept. for the homepage design, the main focus will be B2Consumer Our current page is too blended, lacks reassurance elements and I would like to have a look at this page. from our current stories. here is a link for our business book to give you a feel for it: http://online.pagewavo.com/qtlk/pzme/ MAIN PAGES TO REVIEW / HOMEPAGE / https://pebblelanternkids.co.uk/ BOOKS: https : //pebblelanternkids.co.uk/product-category/personalised-books/ MUSIC: https://pebblelanternkids.co.uk/product-category/music-cds/ BLOG: https://pebblelanternkids.co.uk/blog -2 / Looking forward to seeing you and your questions asap

Target Market(s)

parents and grandparents of children aged 0 to 10 years old. This is for the European market

Industry/Entity Type

Publishing Company

Number of Pages Required

4 page

Colors
0392cd
9bcb3b
ec1f27
757575

Requirements
Must have
• keep within the color code of our RGB logo: D25028 RGB: 8CC364 329BC8 808285
Nice to have
• be more with the style of our competitors. Pebble Lantern Kids am about making children learn the fun way, and develop their morality, self-esteem and confidence. It's about the magic of reading to help children learn while having fun. I have attached visuals but those are just examples and you we encourage you to suggest other ideas

```html
<!DOCTYPE html>
<html lang="en">
<head>
<meta charset="utf-8">
<title>Pebble Lantern Kids — Personalised Stories for Children</title>
<link href="https://fonts.googleapis.com/css2?family=Fira+Sans:wght@400;500;600&family=Fira+Sans+Condensed:wght@500;600;700&display=swap" rel="stylesheet">
<style>
:root{
  --orange:#d25028;
  --red:#ec1f27;
  --green:#8cc364;
  --green-bright:#9bcb3b;
  --blue:#329bc8;
  --blue-deep:#0392cd;
  --teal:#1a9bb0;
  --yellow:#f6b81a;
  --grey:#808285;
  --text:#757575;
  --ink:#4a4a4a;
  --cream:#fdf8e4;
  --paper:#f3f3f3;
  --white:#ffffff;
}
*{box-sizing:border-box;margin:0;padding:0}
html,body{width:1200px;height:3922px;overflow:hidden}
body{position:relative;background:var(--white);font-family:"Fira Sans",Arial,sans-serif;color:var(--text);font-size:14px}
.abs{position:absolute}
.heading{font-family:"Fira Sans Condensed","Arial Narrow",sans-serif;font-weight:600;color:var(--ink);text-align:center;font-size:34px;letter-spacing:.2px}
.btn-outline{display:inline-block;border:2px solid var(--orange);color:var(--orange);font-weight:600;font-size:13px;padding:7px 22px;background:var(--white);border-radius:2px}
.photo{border-radius:8px}

/* header */
.site-header{left:0;top:0;width:1200px;height:204px;background:var(--cream)}
.brand{left:70px;top:20px;display:flex;align-items:center;gap:12px}
.brand-mark{width:44px;height:44px;border-radius:50%;background:var(--orange)}
.brand-name{font-family:"Fira Sans Condensed",sans-serif;font-weight:700;font-size:26px;color:var(--blue);line-height:1.05;width:150px}
.call{left:510px;top:68px;font-size:15px;color:var(--orange);font-weight:600;display:flex;align-items:center;gap:6px}
.socials{display:flex;gap:8px}
.social-sq{width:18px;height:18px;border-radius:3px;background:var(--grey)}
.header-social{left:712px;top:68px}
.lang{left:878px;top:62px;width:98px;height:30px;background:var(--green);color:#fff;font-size:12px;font-weight:600;border-radius:3px;display:flex;align-items:center;padding-left:12px;gap:24px}
.cart{left:990px;top:62px;width:126px;height:30px;background:var(--orange);color:#fff;font-size:12px;font-weight:600;border-radius:3px;display:flex;align-items:center;justify-content:center;gap:6px}
.nav{left:322px;top:148px;display:flex;gap:6px}
.nav a{display:block;height:54px;width:126px;color:#fff;text-decoration:none;font-family:"Fira Sans Condensed",sans-serif;font-weight:600;font-size:16px;text-align:center;padding-top:20px;border-radius:4px 4px 0 0}
.nav .home{background:var(--orange);text-decoration:underline}
.nav .about{background:var(--blue)}
.nav .products{background:var(--teal)}
.nav .distributors{background:var(--green)}
.nav .blog{background:var(--yellow)}
.nav .contact{background:#ee6a2a}

/* hero */
.hero{left:0;top:204px;width:1200px;height:476px;background:linear-gradient(100deg,#b48b63 0%,#c9a57c 40%,#a88259 75%,#8c6a48 100%)}
.hero-title{left:0;top:120px;width:1200px;text-align:center;color:#fff;font-family:"Fira Sans Condensed",sans-serif;font-weight:600;font-size:44px;line-height:1.2;text-shadow:0 2px 6px rgba(0,0,0,.25)}
.story-form{left:131px;top:261px;width:935px;height:79px;background:rgba(255,255,255,.85);border-radius:3px}
.field{top:25px;height:30px;background:#fff;border:1px solid #ddd;font-size:12px;color:#999;padding:7px 10px}
.field .caret{position:absolute;right:10px;top:9px;width:8px;height:8px;border-right:1px solid #999;border-bottom:1px solid #999;transform:rotate(45deg)}
.create{left:708px;top:25px;width:204px;height:30px;background:var(--orange);color:#fff;font-size:12px;font-weight:600;text-align:center;padding-top:8px}

/* welcome */
.welcome{left:0;top:680px;width:1200px;height:379px;background:var(--paper)}
.welcome .heading .name{color:var(--orange)}
.welcome p{font-size:12.5px;line-height:1.6;text-align:center;width:820px;margin:0 auto}

/* how */
.how{left:0;top:1059px;width:1200px;height:347px;background:#fff}
.step{width:190px;text-align:center}
.step-circle{width:94px;height:94px;border-radius:50%;border:3px solid;margin:0 auto;display:flex;align-items:center;justify-content:center;background:#fff}
.step p{margin-top:18px;font-size:13px;font-weight:600;color:var(--ink);line-height:1.45}
.dash{height:0;border-top:2px dashed #bbb;width:94px;top:170px}

/* products */
.products{left:0;top:1398px;width:1200px;height:497px;background:var(--blue)}
.products .heading{color:#fff}
.prod{width:290px;height:320px}
.prod-circle{width:270px;height:270px;border-radius:50%;border:6px solid #fff;margin:0 auto;overflow:hidden}
.prod-label{position:absolute;left:10px;top:210px;width:270px;height:70px;color:#fff;font-family:"Fira Sans Condensed",sans-serif;font-weight:600;font-size:20px;text-align:center;padding-top:22px;border:4px solid #fff;transform:skewY(-3deg)}

/* feature */
.feature h3{font-family:"Fira Sans Condensed",sans-serif;font-weight:600;font-size:24px;color:var(--ink);line-height:1.25}
.feature p{font-size:12.5px;line-height:1.6;margin-top:16px}

/* gallery */
.gallery{left:0;top:2305px;width:1200px;height:630px;background:var(--green-bright)}
.gallery .heading{color:#fff}

/* blog */
.blog-date{font-size:12px;color:var(--blue);font-weight:600}
.blog-title{font-family:"Fira Sans Condensed",sans-serif;font-weight:600;font-size:21px;color:var(--ink);line-height:1.25;text-decoration:underline}
.arrow{width:22px;height:22px;border-left:2px solid #aaa;border-bottom:2px solid #aaa}

/* footer */
.footer{left:0;top:3587px;width:1200px;height:335px;background:var(--blue-deep);color:#fff}
.footer h4{font-family:"Fira Sans Condensed",sans-serif;font-weight:600;font-size:16px;padding-bottom:10px;border-bottom:1px solid rgba(255,255,255,.45);width:255px}
.footer p,.footer li{font-size:12.5px;line-height:1.75;list-style:none}
.footer .call-big{font-weight:600;font-size:17px}
.newsletter{width:280px;height:30px;background:rgba(255,255,255,.85);font-size:12px;color:#777;padding:7px 10px}
.send{width:100px;height:30px;background:var(--orange);font-size:12px;font-weight:600;text-align:center;padding-top:7px}
.footer .social-sq{background:#fff}
</style>
</head>
<body>

<header class="abs site-header">
  <div class="abs brand"><span class="brand-mark"></span><span class="brand-name">Pebble Lantern Kids</span></div>
  <div class="abs call">
    <svg width="16" height="16" viewBox="0 0 24 24"><path fill="#d25028" d="M6.6 10.8a15 15 0 0 0 6.6 6.6l2.2-2.2c.3-.3.7-.4 1-.2 1.1.4 2.3.6 3.6.6.6 0 1 .4 1 1V20c0 .6-.4 1-1 1A17 17 0 0 1 3 4c0-.6.4-1 1-1h3.5c.6 0 1 .4 1 1 0 1.2.2 2.4.6 3.6.1.3 0 .7-.2 1z"/></svg>
    Call Us: 123 - 456 - 7890
  </div>
  <div class="abs socials header-social"><span class="social-sq"></span><span class="social-sq" style="background:var(--red)"></span><span class="social-sq"></span><span class="social-sq"></span><span class="social-sq"></span></div>
  <div class="abs lang"><span>ENG</span><span>▾</span></div>
  <div class="abs cart">
    <svg width="15" height="14" viewBox="0 0 24 22"><path fill="none" stroke="#fff" stroke-width="2.4" d="M1 2h4l3 12h12l3-9H7"/><circle cx="10" cy="19" r="2" fill="#fff"/><circle cx="18" cy="19" r="2" fill="#fff"/></svg>
    My Cart $0.00
  </div>
  <nav class="abs nav">
    <a class="home">Home</a><a class="about">About Us</a><a class="products">Products</a><a class="distributors">Distributors</a><a class="blog">Blog</a><a class="contact">Contact Us</a>
  </nav>
</header>

<section class="abs hero" role="img" aria-label="Child in aviator goggles and blue scarf playing in a cardboard box beside a personalised storybook">
  <h1 class="abs hero-title">Create Personalised Stories<br>for Children</h1>
  <form class="abs story-form">
    <div class="abs field" style="left:26px;width:204px">Your Children Name</div>
    <div class="abs field" style="left:253px;width:204px">English<span class="caret"></span></div>
    <div class="abs field" style="left:478px;width:207px">Boy<span class="caret"></span></div>
    <div class="abs create">Create Your Story</div>
  </form>
</section>

<section class="abs welcome">
  <h2 class="heading" style="margin-top:78px">Welcome to <span class="name">Pebble Lantern Kids</span></h2>
  <p style="margin-top:26px">Is to make children the heroes of the adventure and live magical and unforgettable moments they can share with their family and friends. Scenarios are adapted to every age, imagined and conceived in association with children, schools, speech therapists, psychologists and childhood experts.</p>
  <p style="margin-top:12px">Personalisation offers for children to have an opportunity to recognise themselves in the story, thus developing the morale, self-esteem and confidence. All our stories aim to stimulate learning and enhance reading passion.</p>
  <div style="text-align:center;margin-top:26px"><span class="btn-outline">Discover About</span></div>
</section>

<section class="abs how">
  <h2 class="heading" style="margin-top:60px">How Does it Work?</h2>
  <div class="abs step" style="left:161px;top:122px">
    <div class="step-circle" style="border-color:var(--blue)">
      <svg width="46" height="46" viewBox="0 0 46 46"><circle cx="23" cy="17" r="10" fill="#f0a35a"/><path d="M6 44c2-12 9-16 17-16s15 4 17 16z" fill="#d25028"/></svg>
    </div>
    <p>Write the name of the<br>character.</p>
  </div>
  <div class="abs step" style="left:391px;top:122px">
    <div class="step-circle" style="border-color:var(--green)">
      <svg width="48" height="42" viewBox="0 0 48 42"><path d="M24 2C11 2 2 10 2 20s8 19 18 19c4 0 4-3 2-5s0-6 4-6h8c7 0 12-4 12-10C46 9 36 2 24 2z" fill="#c98b4a"/><circle cx="13" cy="18" r="3.5" fill="#ec1f27"/><circle cx="21" cy="10" r="3.5" fill="#f6b81a"/><circle cx="32" cy="11" r="3.5" fill="#329bc8"/><circle cx="37" cy="20" r="3.5" fill="#8cc364"/></svg>
    </div>
    <p>Personalise their<br>appearance.</p>
  </div>
  <div class="abs step" style="left:619px;top:122px">
    <div class="step-circle" style="border-color:var(--orange)">
      <svg width="48" height="42" viewBox="0 0 48 42"><rect x="3" y="5" width="36" height="28" rx="2" fill="#4a4a4a"/><path d="M7 29l10-12 7 8 5-5 6 9z" fill="#9bcb3b"/><circle cx="38" cy="32" r="9" fill="#8cc364"/><path d="M38 27v10M33 32h10" stroke="#fff" stroke-width="2.5"/></svg>
    </div>
    <p>Add a picture and a<br>dedication</p>
  </div>
  <div class="abs step" style="left:846px;top:122px">
    <div class="step-circle" style="border-color:var(--grey)">
      <svg width="44" height="44" viewBox="0 0 44 44"><path d="M8 14l18-8 12 10-18 8z" fill="#f6b81a"/><path d="M8 14v16l12 8V24z" fill="#d59a14"/><path d="M20 24v14l18-10V16z" fill="#e8aa18"/></svg>
    </div>
    <p>Conveniently receive it<br>at your home.</p>
  </div>
  <div class="abs dash" style="left:325px"></div>
  <div class="abs dash" style="left:555px"></div>
  <div class="abs dash" style="left:783px"></div>
</section>

<section class="abs products">
  <svg class="abs" style="left:0;top:-2px" width="1200" height="30" viewBox="0 0 1200 30" preserveAspectRatio="none">
    <path fill="#fff" d="M0 0H1200V10 Q1185 26 1170 10 Q1155 26 1140 10 Q1125 26 1110 10 Q1095 26 1080 10 Q1065 26 1050 10 Q1035 26 1020 10 Q1005 26 990 10 Q975 26 960 10 Q945 26 930 10 Q915 26 900 10 Q885 26 870 10 Q855 26 840 10 Q825 26 810 10 Q795 26 780 10 Q765 26 750 10 Q735 26 720 10 Q705 26 690 10 Q675 26 660 10 Q645 26 630 10 Q615 26 600 10 Q585 26 570 10 Q555 26 540 10 Q525 26 510 10 Q495 26 480 10 Q465 26 450 10 Q435 26 420 10 Q405 26 390 10 Q375 26 360 10 Q345 26 330 10 Q315 26 300 10 Q285 26 270 10 Q255 26 240 10 Q225 26 210 10 Q195 26 180 10 Q165 26 150 10 Q135 26 120 10 Q105 26 90 10 Q75 26 60 10 Q45 26 30 10 Q15 26 0 10Z"/>
  </svg>
  <h2 class="heading" style="margin-top:80px">Our Products</h2>
  <div class="abs prod" style="left:145px;top:148px">
    <div class="prod-circle" role="img" aria-label="Two children lying on the floor reading a book together" style="background:linear-gradient(160deg,#f4f1ee,#e9c7b0 60%,#c46b4e)"></div>
    <div class="prod-label" style="background:var(--blue)">Books</div>
  </div>
  <div class="abs prod" style="left:455px;top:148px">
    <div class="prod-circle" role="img" aria-label="Excited girl wearing headphones listening to music" style="background:linear-gradient(160deg,#f6f0f4,#f1c9c0 55%,#e59fb2)"></div>
    <div class="prod-label" style="background:var(--orange)">Music CD</div>
  </div>
  <div class="abs prod" style="left:765px;top:148px">
    <div class="prod-circle" role="img" aria-label="Smiling boy lying on a bed holding a remote control" style="background:linear-gradient(160deg,#f4f4f2,#e2d4c2 55%,#7fa6c4)"></div>
    <div class="prod-label" style="background:var(--blue)">DVD Cartoon</div>
  </div>
</section>

<section class="abs feature" style="left:230px;top:1978px;width:340px">
  <h3>Personalisation Improves<br>a Child's Learning Ability And<br>Motivation</h3>
  <p>Pebble Lantern Kids personalised books offers the possibility of sharing magical and unique moments which help the child become familiar with reading and inspire reading passion. Which is more special and magical than becoming the hero of your own story!</p>
  <div style="margin-top:22px"><span class="btn-outline">Learn More</span></div>
</section>
<div class="abs photo" role="img" aria-label="Child in a knitted hat sitting on a toy chest holding a personalised book, video still" style="left:614px;top:1962px;width:354px;height:274px;border-radius:2px;background:linear-gradient(135deg,#d9d3cb,#b8a592 55%,#7a5848)">
  <svg class="abs" style="left:157px;top:117px" width="40" height="40" viewBox="0 0 40 40"><circle cx="20" cy="20" r="19" fill="rgba(255,255,255,.85)"/><path d="M16 12l12 8-12 8z" fill="#4a4a4a"/></svg>
</div>

<section class="abs gallery">
  <h2 class="heading" style="margin-top:64px">Enjoy Your Personalised Story</h2>
  <div class="abs photo" role="img" aria-label="Child with goggles and scarf playing in a cardboard box with a storybook" style="left:157px;top:134px;width:431px;height:201px;background:linear-gradient(110deg,#b48b63,#cfae86 55%,#9c7651)"></div>
  <div class="abs photo" role="img" aria-label="Young boy holding up his personalised book" style="left:612px;top:134px;width:204px;height:201px;background:linear-gradient(150deg,#6e8a5a,#9db07c 50%,#d3a254)"></div>
  <div class="abs photo" role="img" aria-label="Parent and child laughing while reading together" style="left:839px;top:134px;width:207px;height:201px;background:linear-gradient(150deg,#e9dfd2,#d2b49a 55%,#a07c62)"></div>
  <div class="abs photo" role="img" aria-label="Boy holding a personalised book cover" style="left:157px;top:361px;width:209px;height:202px;background:linear-gradient(150deg,#4f7fa3,#8aaac3 55%,#c8b79f)"></div>
  <div class="abs photo" role="img" aria-label="Mother kissing a child holding an open book" style="left:384px;top:361px;width:204px;height:202px;background:linear-gradient(150deg,#d8c6b6,#b98f73 55%,#6d5444)"></div>
  <div class="abs photo" role="img" aria-label="Mother and daughter reading on the floor at home" style="left:612px;top:361px;width:434px;height:202px;background:linear-gradient(110deg,#ece9e4,#d6ccc2 50%,#8a6f5e)"></div>
</section>

<section class="abs" style="left:0;top:2935px;width:1200px;height:652px">
  <h2 class="heading" style="margin-top:60px">Latest Blog</h2>
  <div class="abs photo" role="img" aria-label="Little girl in a festive hat" style="left:235px;top:155px;width:150px;height:205px;border-radius:14px;background:linear-gradient(150deg,#d9e6ef,#e7b7a5 55%,#c94a3c)"></div>
  <div class="abs photo" role="img" aria-label="Two smiling children together" style="left:818px;top:155px;width:150px;height:205px;border-radius:14px;background:linear-gradient(150deg,#eef0f3,#d9c6b0 55%,#b49168)"></div>
  <div class="abs photo" role="img" aria-label="Mother lifting a laughing baby" style="left:387px;top:131px;width:429px;height:249px;border-radius:14px;background:linear-gradient(120deg,#e7ecec,#d8c3b2 50%,#a88876);box-shadow:0 4px 12px rgba(0,0,0,.12)"></div>
  <div class="abs arrow" style="left:168px;top:243px;transform:rotate(45deg)"></div>
  <div class="abs arrow" style="left:1013px;top:243px;transform:rotate(-135deg);border-color:var(--orange)"></div>
  <div class="abs" style="left:387px;top:405px;width:440px">
    <div class="blog-date">30 Sep, 2018 &nbsp;/&nbsp; By: Admin</div>
    <div class="blog-title" style="margin-top:8px">There are many variations of passages of Lorem Ipsum available</div>
    <p style="font-size:12.5px;line-height:1.6;margin-top:12px">Lorem ipsum dolor sit amet, consectetur adipiscing elit. Quisque cursus, sem eget sagittis sagittis, nisl magna sodales eros.</p>
  </div>
  <div class="abs" style="left:0;top:565px;width:1200px;text-align:center"><span class="btn-outline">View All</span></div>
</section>

<footer class="abs footer">
  <div class="abs" style="left:157px;top:58px">
    <h4>Contact Us</h4>
    <p style="margin-top:14px">4108 Orchard Bend Road Fallowmere,<br>MI 33537</p>
    <p class="call-big">Call Us: 123 - 456 - 7890</p>
    <p style="text-decoration:underline">hello@pebblelanternkids.com</p>
  </div>
  <div class="abs" style="left:457px;top:58px">
    <h4>Our Collections</h4>
    <ul style="margin-top:14px">
      <li>Personalised Books</li><li>Personalised Music Albums</li><li>Personalised DVD Cartoon</li><li>Personalised School books</li>
    </ul>
  </div>
  <div class="abs" style="left:763px;top:58px">
    <h4>Sign Up Newsletter</h4>
    <div class="newsletter" style="margin-top:18px">Enter Your Email...</div>
    <div class="send" style="margin-top:12px">▸ Send</div>
  </div>
  <div class="abs" style="left:157px;top:248px;width:886px;border-top:1px solid rgba(255,255,255,.45)"></div>
  <p class="abs" style="left:157px;top:278px">© 2018 Pebble Lantern Kids. All Right Reserved.</p>
  <p class="abs" style="left:457px;top:278px">Terms &amp; Conditions &nbsp;&nbsp;|&nbsp;&nbsp; Privacy Policy</p>
  <div class="abs socials" style="left:763px;top:281px"><span class="social-sq"></span><span class="social-sq"></span><span class="social-sq"></span><span class="social-sq"></span><span class="social-sq"></span></div>
  <svg class="abs" style="left:1020px;top:280px" width="22" height="22" viewBox="0 0 22 22"><circle cx="11" cy="11" r="10" fill="#fff"/><path d="M6 13l5-5 5 5" fill="none" stroke="#0392cd" stroke-width="2"/></svg>
</footer>

</body>
</html>
```